Corwin Halvey Golf Instruction

I need a web design for a golf instruction website. My goal is to gain more exposure through this site. I want this site to be a source for golf knowledge and instruction by providing instructional videos and instructional literature. I want the site to have colors navy blue(tulsa ravens blue) and silver. I am also open to other color schemes. The main website to imitate is deklanmorrowby.example. I want tabs/links at the top of the site that read: Home, About, Video Instruction, Instruction, and Golf Blog. Other sites to reference are Pell Vostrand Golf and truearcbirdieplay.example. A main feature that must be included is online video lessons like on pellvostrand.example. I have software that provides me the ability to take a video of a golf swing and record a voice video lesson. Reference the example video on pellvostrand.example.

The main goal for this web design is to have an "outline" in place so that I can go back and input the videos and literature.

Reason: I need more time to wait for changes. I like all the designs.

Target Market(s)

My target market is golfer of all ages and abilities: juniors, adults, men, and women.

Industry/Entity Type

Software

Requirements
Must have
• Capability to input videos and literature onto the site.
"Lead Instructor at Marlpit Golf Club" title.
A very visible "Marlpit Golf Club" logo.
Friendbook, Chirp, and ClipTube quicklinks.

```html
<!DOCTYPE html>
<html lang="en">
<head>
<meta charset="utf-8">
<title>Corwin Halvey Golf Instruction</title>
<link rel="stylesheet" href="https://fonts.googleapis.com/css2?family=Source+Sans+3:wght@400;600;700&family=Yanone+Kaffeesatz:wght@400;700&family=PT+Sans+Narrow:wght@700&display=swap">
<style>
:root{
  --black:#0b0b0b;
  --header:#151515;
  --page:#e8eae9;
  --white:#ffffff;
  --ink:#1f1f1f;
  --muted:#555;
  --link:#2b9fd6;
  --green:#7fb521;
  --green-dark:#4e7d10;
  --orange:#f2b733;
  --lime:#9ccc2a;
  --blue-box:#3aa0cf;
  --dark-card:#2b2b2b;
  --nav:#3fb3ec;
  --line:#b9bcbb;
}
*{box-sizing:border-box;margin:0;padding:0}
html,body{width:976px;height:1200px;overflow:hidden}
body{position:relative;background:var(--page);font-family:"Source Sans 3",Arial,sans-serif;color:var(--ink)}
.abs{position:absolute}
a{text-decoration:none;color:var(--link)}

/* header */
.site-header{position:absolute;left:0;top:0;width:976px;height:66px;background:radial-gradient(ellipse at 40% 40%,#2a2a2a,var(--header) 70%)}
.brand{left:182px;top:8px;width:210px;color:#d7d9dc;font-size:21px;font-weight:600;line-height:22px;display:flex;align-items:center;gap:6px}
.brand-dot{width:10px;height:10px;border-radius:50%;background:#d7d9dc;flex:none}
.top-nav{right:193px;top:4px;display:flex;gap:18px;font-size:7.5px}
.top-nav a{color:var(--nav)}
.tab-events{left:533px;top:32px;width:138px;height:34px;background:var(--orange);transform:rotate(-2deg);color:#3a2a00;font-size:11px;padding:10px 0 0 14px}
.tab-social{left:667px;top:40px;width:116px;height:26px;background:var(--lime);display:flex;gap:4px;align-items:center;padding-left:22px}
.tab-social span{background:#2e6fb0;color:#fff;font-size:6.5px;font-weight:600;padding:3px 3px;border-radius:2px}

/* hero (children positioned inside the hero box) */
.hero{left:0;top:66px;width:976px;height:318px;background:linear-gradient(180deg,#9fc4e8 0%,#5c8a3a 18%,#2f6e22 45%,#4f9a35 75%,#3b7a28 100%)}
.hero-photo{left:187px;top:54px;width:263px;height:150px;background:#fff;padding:5px 5px 18px;transform:rotate(-2deg);box-shadow:0 2px 6px rgba(0,0,0,.4)}
.hero-photo div{width:100%;height:100%;background:linear-gradient(180deg,#2f6f1d,#4caa2e 60%,#3e8f24)}
.hero-title{left:484px;top:59px;width:296px;text-align:center;font-family:"Yanone Kaffeesatz",sans-serif;font-weight:700;font-size:28px;line-height:21px;color:#fff;text-shadow:0 1px 3px rgba(0,0,0,.5)}
.hero-text{left:478px;top:112px;width:292px;font-size:10.5px;line-height:11.5px;color:#fff;text-shadow:0 1px 2px rgba(0,0,0,.5)}
.hero-text p+p{margin-top:11px}
.hero-ball{left:713px;top:194px;width:54px;height:54px;border-radius:50%;background:radial-gradient(circle at 40% 35%,#fff,#c9d3db)}
.hero-more{left:703px;top:211px;width:80px;height:20px;border-radius:10px;background:linear-gradient(#7fd0f0,#2d9fd0);color:#0d3e55;font-size:10.5px;text-align:center;line-height:20px}
.slider-dots{left:437px;top:278px;width:91px;height:17px;border-radius:9px;background:rgba(0,0,0,.25);display:flex;gap:5px;align-items:center;padding-left:6px}
.slider-dots i{width:12px;height:12px;border-radius:50%;background:#3c4a3a;display:block}
.slider-dots i:first-child{background:var(--green)}

/* booking */
.intro{left:180px;top:402px;font-size:11.5px;line-height:15.5px}
.field{height:22px;background:#fff;border:1px solid #c9cccb;font-size:7.5px;color:#444;padding:7px 6px;position:absolute;line-height:8px}
.btn-green{position:absolute;border-radius:10px;background:linear-gradient(#9ad132,var(--green-dark));color:#12300a;font-size:8px;font-weight:700;text-align:center}
.select-arrow{position:absolute;right:0;top:0;width:22px;height:20px;border-left:1px solid #ccc}
.select-arrow:after{content:"";position:absolute;left:7px;top:8px;border:4px solid transparent;border-top-color:#777}

/* video */
.video-card{left:179px;top:481px;width:393px;height:254px;background:#fff}
.video{left:14px;top:11px;width:362px;height:206px;background:linear-gradient(180deg,#8b8fb8 0%,#c9a9a8 25%,#3e6a33 45%,#5a8f40 75%,#2f5a28 100%)}
.video-play{left:164px;top:78px}
.video-bar{left:0;bottom:0;width:362px;height:26px;background:rgba(20,20,20,.85)}
.caption{left:11px;top:226px;width:370px;font-size:10px;line-height:11.5px}

/* articles */
.article{left:180px;width:392px}
.article h2{font-weight:400;font-size:16px;line-height:18px;margin-bottom:5px}
.article p{font-size:9.2px;line-height:11.5px;color:#333}
.article small{font-size:9px;color:#666}
.rule{left:180px;width:392px;height:2px;background:var(--line)}

/* sidebar */
.side-h{font-family:"PT Sans Narrow",sans-serif;font-weight:700;font-size:13px;line-height:14px;color:#222}
.side-p{font-size:9.2px;line-height:11.5px;color:#333}
.mobile-card{left:588px;top:556px;width:203px;height:126px;background:var(--dark-card);transform:rotate(.6deg);box-shadow:2px 3px 3px rgba(0,0,0,.3)}
.mobile-title{left:82px;top:12px;color:#fff;font-size:21px;font-weight:400;line-height:19px;letter-spacing:-.5px}
.mobile-sub{left:68px;top:55px;color:#3aa0cf;font-size:10px;line-height:11px;width:132px}
.mobile-note{left:0;top:92px;width:203px;text-align:center;color:#8ac23a;font-size:7.5px;line-height:11px}
.events{left:591px;top:764px;width:199px;height:206px;background:var(--blue-box)}
.event{position:absolute;left:9px;width:185px;display:flex;gap:8px;line-height:11.5px}
.event .thumb{width:53px;height:48px;flex:none;border:2px solid #2a2a2a;background:linear-gradient(180deg,#5e8b40,#8fbf5a 55%,#cfd8c6)}
.event b{display:block;font-size:9.5px;line-height:12px;color:#fff}
.event span{display:block;font-size:8.5px;line-height:11.5px;color:#fff}

/* footer */
.site-footer{left:0;top:1025px;width:976px;height:175px;background:radial-gradient(ellipse at 50% 40%,#262626,var(--black) 75%)}
.foot-nav{right:192px;top:5px;display:flex;gap:18px;font-size:7.5px}
.foot-nav a{color:var(--nav)}
.foot-h{left:180px;top:18px;color:#fff;font-size:11px}
.gallery{left:177px;top:47px;display:flex;gap:6.5px}
.gallery div{width:96px;height:69px;border:2px solid #ddd}
.arrow{top:78px;color:#fff;font-size:14px}
.share{top:150px;display:flex;gap:12px;left:180px}
.share span{background:#e8e8e8;color:#333;font-size:7px;padding:2px 5px;border:1px solid #999}
.copy{top:155px;color:#888;font-size:7px;right:200px}
</style>
</head>
<body>

<header class="site-header">
  <div class="abs brand"><span class="brand-dot"></span>Corwin Halvey Golf Instruction</div>
  <nav class="abs top-nav"><a href="#">Home</a><a href="#">About</a><a href="#">Video Instruction</a><a href="#">Instruction</a><a href="#">Golf Blog</a></nav>
  <div class="abs tab-events">golf and tournaments</div>
  <div class="abs tab-social"><span>Chirp</span><span>Friendbook</span><span>ClipTube</span></div>
</header>

<section class="abs hero" role="img" aria-label="Wide view of a green golf course with sand bunkers and trees">
  <div class="abs hero-photo"><div role="img" aria-label="Golfer putting a ball toward the hole"></div></div>
  <h1 class="abs hero-title">“Lead Instructor at Marlpit Golf Club”</h1>
  <div class="abs hero-text">
    <p>Fusce auctor nulla eget lacus pretium imperdiet ultrices turpis varius. Nunc justo nibh, tincidunt ut ullamcorper condimentum, dignissim id sapien. Fusce auctor nulla eget lacus pretium imperdiet ultrices turpis varius.</p>
    <p>Nunc justo nibh, tincidunt ut ullamcorper condimentum, dignissim id sapien.</p>
  </div>
  <div class="abs hero-ball"></div>
  <a class="abs hero-more" href="#">read more!</a>
  <div class="abs slider-dots"><i></i><i></i><i></i><i></i><i></i></div>
</section>

<main>
  <p class="abs intro">Lorem ipsum dolor sit amet<br>consectetuer adipiscing elit, sed diam nonummy nibh euismod</p>
  <div class="field" style="left:180px;top:442px;width:171px">Select your desired date</div>
  <div class="field" style="left:357px;top:442px;width:128px">Number of players<span class="select-arrow"></span></div>
  <div class="btn-green" style="left:492px;top:443px;width:80px;height:20px;line-height:20px">Submit</div>

  <div class="abs video-card">
    <div class="abs video" role="img" aria-label="Aerial view of a golf course with a lake at sunset">
      <svg class="abs video-play" width="34" height="36" viewBox="0 0 34 36"><path d="M2 2 L32 18 L2 34Z" fill="#fff"/></svg>
      <div class="abs video-bar">
        <svg width="362" height="26"><rect x="6" y="5" width="44" height="16" fill="#111"/><path d="M24 9 L31 13 L24 17Z" fill="#fff"/><rect x="60" y="9" width="250" height="6" fill="#555"/><rect x="60" y="9" width="84" height="6" fill="#2b9fd6"/><g fill="#2b9fd6"><rect x="320" y="8" width="2" height="9"/><rect x="324" y="8" width="2" height="9"/><rect x="328" y="8" width="2" height="9"/><rect x="332" y="8" width="2" height="9"/><rect x="336" y="8" width="2" height="9"/><rect x="340" y="8" width="2" height="9"/></g><rect x="348" y="9" width="7" height="7" fill="none" stroke="#fff"/></svg>
      </div>
    </div>
    <p class="abs caption">Lorem ipsum dolor sit amet, consectetuer adipiscing elit, sed diam nonummy nibh euismod tincidunt ut <a href="#">laoreet dolore</a> magna aliquam</p>
  </div>

  <article class="abs article" style="top:752px">
    <h2>Lorem ipsum dolor sit amet, consectetuer adipiscing elit</h2>
    <p>Lorem ipsum dolor sit amet, consectetuer adipiscing elit, sed diam nonummy nibh euismod tincidunt ut Lorem ipsum dolor sit amet, consectetuer adipiscing elit, laoreet dolore magna aliquam erat volutpat. Ut wisi enim Lorem ipsum dolor sit amet, consectetuer adipiscing elit...<br><a href="#">read more ›</a></p>
  </article>
  <div class="abs rule" style="top:823px"></div>
  <article class="abs article" style="top:837px">
    <h2>Lorem ipsum dolor sit amet</h2>
    <p style="color:#111">Lorem ipsum dolor sit amet, consectetuer adipiscing elit, sed diam nonummy nibh euismod tincidunt ut Lorem ipsum dolor sit amet, consectetuer adipiscing elit, laoreet dolore magna aliquam erat volutpat. Ut wisi enim Lorem ipsum dolor sit amet,.. <a href="#">read more ›</a></p>
  </article>
  <div class="abs rule" style="top:909px"></div>
  <article class="abs article" style="top:921px">
    <h2>Mira Castellane leads WPGT Championship <small>Posted by Renna</small></h2>
    <p>There are many variations of passages of Lorem Ipsum available, but the majority have suffered alteration in some form, by injected humour, or randomised words which don't look even slightly believable. If you are going to use a passage of Lorem Ipsum... <a href="#"><b>read more ›</b></a></p>
  </article>
</main>

<aside>
  <h3 class="abs side-h" style="left:596px;top:401px">EMAIL UPDATES</h3>
  <p class="abs side-p" style="left:596px;top:417px;width:185px">Lorem Ipsum is simply dummy text of the printing and typesetting industry.</p>
  <div class="field" style="left:596px;top:453px;width:187px">First Name</div>
  <div class="field" style="left:596px;top:481px;width:187px">Email</div>
  <svg class="abs" style="left:597px;top:520px" width="14" height="13" viewBox="0 0 14 13"><path d="M7 0 L14 13 H0Z" fill="#111"/><rect x="6.2" y="4.5" width="1.6" height="4.5" fill="#fff"/><rect x="6.2" y="10" width="1.6" height="1.6" fill="#fff"/></svg>
  <div class="btn-green" style="left:703px;top:515px;width:80px;height:20px;line-height:20px">subscribe</div>

  <div class="abs mobile-card">
    <svg class="abs" style="left:10px;top:12px" width="72" height="66" viewBox="0 0 72 66"><rect x="2" y="2" width="50" height="62" rx="6" fill="#fff"/><rect x="8" y="8" width="38" height="38" fill="#2b2b2b"/><circle cx="27" cy="55" r="4" fill="#2b2b2b"/><circle cx="27" cy="22" r="6" fill="#3aa0cf"/><path d="M16 40 Q27 26 38 40Z" fill="#3aa0cf"/><path d="M46 26 L58 16 V22 H70 V30 H58 V36Z" fill="#fff"/></svg>
    <div class="abs mobile-title">Mobile<br>and Simple</div>
    <div class="abs mobile-sub">Want discounts sent directly to your phone?</div>
    <div class="abs mobile-note">Text "lovegolf" (without quotes) to 40219<br>Don't worry, we won't spam!</div>
  </div>

  <h3 class="abs side-h" style="left:596px;top:697px">EVENT CALENDAR</h3>
  <p class="abs side-p" style="left:596px;top:713px;width:190px">Click on the events below to find out about our upcoming tournaments and events. Or you can view <a href="#"><b>all events</b></a> that we have coming.</p>

  <svg class="abs" style="left:752px;top:751px" width="20" height="14"><path d="M0 14 L4 0 L20 14Z" fill="#3aa0cf"/></svg>
  <div class="abs events">
    <div class="event" style="top:14px"><div class="thumb" role="img" aria-label="Golf course bunkers"></div><div><b>July 24th, 2012</b><span>There are many variations of passages of Lorem Ipsum available, but the majority...</span></div></div>
    <div class="event" style="top:77px"><div class="thumb" role="img" aria-label="Golf course bunkers"></div><div><b>August 1st, 2012</b><span>There are many variations of passages of Lorem Ipsum available, but the majority...</span></div></div>
    <div class="event" style="top:140px"><div class="thumb" role="img" aria-label="Golf course bunkers"></div><div><b>September 29th, 2012</b><span>There are many variations of passages of Lorem Ipsum available, but the majority...</span></div></div>
  </div>
  <div class="btn-green" style="left:703px;top:962px;width:80px;height:20px;line-height:20px">all events</div>
</aside>

<footer class="abs site-footer">
  <nav class="abs foot-nav"><a href="#">Home</a><a href="#">About</a><a href="#">Video Instruction</a><a href="#">Instruction</a><a href="#">Golf Blog</a></nav>
  <div class="abs foot-h">LOREM IPSUM DOLOR SIT AMET</div>
  <div class="abs arrow" style="left:164px">‹</div>
  <div class="abs gallery">
    <div role="img" aria-label="Golf ball on a tee" style="background:linear-gradient(#7fb0e0,#5fae3a)"></div>
    <div role="img" aria-label="Fairway framed by trees" style="background:linear-gradient(#6a5a45,#4f7a35)"></div>
    <div role="img" aria-label="Golf ball on a green" style="background:linear-gradient(#9cc7e8,#7bbf3a)"></div>
    <div role="img" aria-label="Golf balls on tees" style="background:linear-gradient(#3a6a2a,#8fc24a)"></div>
    <div role="img" aria-label="Aerial course view at dusk" style="background:linear-gradient(#a8a0d0,#4f8a38)"></div>
    <div role="img" aria-label="Course with bunkers" style="background:linear-gradient(#9fbfd8,#3f7f2f)"></div>
  </div>
  <div class="abs arrow" style="left:793px">›</div>
  <div class="abs share"><span>+1</span><span>Like</span><span>Follow</span></div>
  <div class="abs copy">Copyright 2012 Website Name</div>
</footer>

</body>
</html>
```